Bright Summit Consulting Website Design

I already have a live website. Just want some help with design, finishing up the project. I also have another site with wix that I am ready to have designed. I am not completely sure on the pages but will for sure need "coaching", "training", "resources". Most of the people I currently work with are real estate brokers and mortgage brokers but I want to be able to appeal to all industries.
Number of Pages Required
4 page
Font styles to use
Sans Serif
Colors
Designer to choose colors to be used in the design.
Requirements
Must have
- place holders for video
Nice to have
- a way for people to purchase digital downloads

```html
<!DOCTYPE html>
<html lang="en">
<head>
<meta charset="utf-8">
<title>Testimonials | Bright Summit Consulting</title>
<link rel="stylesheet" href="https://fonts.googleapis.com/css2?family=Lato:wght@400;700&display=swap">
<style>
:root{
  --red:#ee2b2b;
  --ink:#333a42;
  --body:#5d6670;
  --muted:#8c949c;
  --line:#e8ebee;
  --band:#f6f8f8;
  --star:#f5a623;
  --avatar:#dce6ea;
  --avatar-ring:#c9d7dd;
  --white:#ffffff;
}
*{box-sizing:border-box;margin:0;padding:0}
html,body{width:1200px;height:2411px;overflow:hidden;background:var(--white)}
body{position:relative;font-family:"Lato",sans-serif;color:var(--ink)}
.abs{position:absolute}
a{color:inherit;text-decoration:none}

/* header */
.brand{left:116px;top:50px;display:flex;align-items:center;gap:10px}
.brand-square{width:24px;height:24px;background:var(--red);flex:none}
.brand-name{font-size:20px;line-height:22px;font-weight:700;color:var(--red)}
.contact{top:24px;font-size:17px;color:var(--ink);display:flex;align-items:center;gap:12px}
.contact.phone{left:605px}
.contact.mail{left:784px}
.main-nav{top:82px;left:383px;font-size:14px;text-transform:uppercase;color:var(--ink)}
.main-nav a{position:absolute;white-space:nowrap}
.cta{left:890px;top:72px;width:193px;height:39px;border-radius:20px;background:var(--red);color:var(--white);font-size:14px;font-weight:700;display:flex;align-items:center;justify-content:center;text-transform:uppercase}

/* hero */
.hero{left:0;top:148px;width:1200px;height:597px;background:linear-gradient(100deg,#4a4540 0%,#6b6259 35%,#5a5f66 65%,#2f3b4a 100%)}
.hero-shade{left:0;top:148px;width:1200px;height:597px;background:rgba(20,25,35,.35)}
.hero-quote{left:150px;top:302px;width:900px;text-align:center;color:var(--white);font-size:32px;line-height:45px}
.hero-name{left:0;top:462px;width:1200px;text-align:center;color:var(--white);font-size:19px;text-transform:uppercase}
.play{left:559px;top:530px}

/* breadcrumb */
.crumbs{left:0;top:745px;width:1200px;height:46px;background:var(--band)}
.crumb-text{left:116px;top:759px;font-size:16px;color:var(--body)}
.crumb-text .current{color:var(--red)}

/* testimonials */
.avatar{width:86px;height:86px;border-radius:50%;background:var(--avatar);border:3px solid var(--avatar-ring)}
.person{font-size:17px;color:var(--ink);text-align:center;width:160px}
.t-title{font-size:27px;font-weight:700;color:var(--ink)}
.t-quote{font-size:17px;color:var(--body);line-height:26px}
.stars{display:flex;gap:8px}
.divider{left:167px;width:863px;height:1px;background:var(--line)}
.pager{left:590px;top:1603px;width:20px;text-align:center;font-size:20px;color:var(--red)}

/* newsletter */
.news{left:0;top:1732px;width:1200px;height:427px;background:linear-gradient(160deg,#6b6560 0%,#8a8278 40%,#5d5650 100%)}
.news-shade{left:0;top:1732px;width:1200px;height:427px;background:rgba(25,28,35,.45)}
.news-title{left:0;top:1840px;width:1200px;text-align:center;color:var(--white);font-size:43px;font-weight:700}
.news-sub{left:0;top:1912px;width:1200px;text-align:center;color:var(--white);font-size:20px}
.field{top:1991px;width:297px;height:53px;border-radius:27px;background:var(--white);color:var(--muted);font-size:20px;padding-left:28px;display:flex;align-items:center}
.subscribe{left:825px;top:1991px;width:192px;height:53px;border-radius:27px;background:var(--red);color:var(--white);font-size:19px;font-weight:700;display:flex;align-items:center;justify-content:center}

/* footer */
.foot-brand{left:185px;top:2232px;font-size:20px;line-height:22px;font-weight:700;color:var(--red)}
.foot-nav a{position:absolute;top:2243px;font-size:20px;color:var(--body)}
.foot-nav a.active{color:var(--red)}
.social{top:2245px;width:22px;height:22px;border-radius:50%}
.copyright{left:0;top:2361px;width:1200px;text-align:center;font-size:13px;color:var(--muted)}
</style>
</head>
<body>

<header>
  <div class="abs brand"><span class="brand-square"></span><span class="brand-name">Bright Summit<br>Consulting</span></div>
  <div class="abs contact phone">
    <svg width="18" height="18" viewBox="0 0 24 24"><path fill="var(--red)" d="M6.6 10.8a15.1 15.1 0 0 0 6.6 6.6l2.2-2.2c.3-.3.7-.4 1-.2 1.1.4 2.3.6 3.6.6.6 0 1 .4 1 1V20c0 .6-.4 1-1 1A17 17 0 0 1 3 4c0-.6.4-1 1-1h3.5c.6 0 1 .4 1 1 0 1.3.2 2.5.6 3.6.1.3 0 .7-.2 1z"/></svg>
    555 014 2280
  </div>
  <div class="abs contact mail">
    <svg width="22" height="16" viewBox="0 0 22 16"><rect width="22" height="16" rx="1" fill="var(--red)"/><path d="M1 1l10 8 10-8" stroke="#fff" stroke-width="1.6" fill="none"/></svg>
    billing@brightsummitconsulting.com
  </div>
  <nav class="abs main-nav">
    <a style="left:0">Home</a>
    <a style="left:67px">About</a>
    <a style="left:141px">Coaching Services</a>
    <a style="left:304px">Resources</a>
    <a style="left:442px">Login</a>
  </nav>
  <a class="abs cta">Start My Training</a>
</header>

<section>
  <div class="abs hero" role="img" aria-label="Photo of a team meeting with colleagues shaking hands across a table"></div>
  <div class="abs hero-shade"></div>
  <p class="abs hero-quote">“Here we can write a quote from the Customer Speech.Lorem ipsum dolor sit amet, consectetur adipiscing elit. Sed fermentum libero felis, et venenatis nunc.”</p>
  <p class="abs hero-name">Grant Ellery</p>
  <svg class="abs play" width="82" height="82" viewBox="0 0 82 82" aria-label="Play video">
    <circle cx="41" cy="41" r="39" fill="none" stroke="#fff" stroke-width="2.5"/>
    <path d="M33 26l23 15-23 15z" fill="#fff"/>
  </svg>
</section>

<div class="abs crumbs"></div>
<p class="abs crumb-text">Home &nbsp;» &nbsp;<span class="current">Testimonials</span></p>

<main>
  <!-- testimonial 1 -->
  <div class="abs avatar" style="left:190px;top:969px" role="img" aria-label="Client avatar"></div>
  <p class="abs person" style="left:153px;top:1066px">Dana Whitfield</p>
  <h3 class="abs t-title" style="left:309px;top:971px">Amazing Speaker</h3>
  <p class="abs t-quote" style="left:313px;top:1018px">“Amazing speaker and motivator. He will light a fire under your a*s!”</p>
  <div class="abs stars" style="left:849px;top:976px">
    <svg width="26" height="26" viewBox="0 0 24 24"><path fill="var(--star)" d="M12 1.5l3.1 7 7.4.6-5.6 4.9 1.7 7.4L12 17.5l-6.6 3.9 1.7-7.4L1.5 9.1l7.4-.6z"/></svg>
    <svg width="26" height="26" viewBox="0 0 24 24"><path fill="var(--star)" d="M12 1.5l3.1 7 7.4.6-5.6 4.9 1.7 7.4L12 17.5l-6.6 3.9 1.7-7.4L1.5 9.1l7.4-.6z"/></svg>
    <svg width="26" height="26" viewBox="0 0 24 24"><path fill="var(--star)" d="M12 1.5l3.1 7 7.4.6-5.6 4.9 1.7 7.4L12 17.5l-6.6 3.9 1.7-7.4L1.5 9.1l7.4-.6z"/></svg>
    <svg width="26" height="26" viewBox="0 0 24 24"><path fill="var(--star)" d="M12 1.5l3.1 7 7.4.6-5.6 4.9 1.7 7.4L12 17.5l-6.6 3.9 1.7-7.4L1.5 9.1l7.4-.6z"/></svg>
    <svg width="26" height="26" viewBox="0 0 24 24"><path fill="var(--star)" d="M12 1.5l3.1 7 7.4.6-5.6 4.9 1.7 7.4L12 17.5l-6.6 3.9 1.7-7.4L1.5 9.1l7.4-.6z"/></svg>
  </div>
  <div class="abs divider" style="top:1134px"></div>

  <!-- testimonial 2 -->
  <div class="abs stars" style="left:195px;top:1193px">
    <svg width="26" height="26" viewBox="0 0 24 24"><path fill="var(--star)" d="M12 1.5l3.1 7 7.4.6-5.6 4.9 1.7 7.4L12 17.5l-6.6 3.9 1.7-7.4L1.5 9.1l7.4-.6z"/></svg>
    <svg width="26" height="26" viewBox="0 0 24 24"><path fill="var(--star)" d="M12 1.5l3.1 7 7.4.6-5.6 4.9 1.7 7.4L12 17.5l-6.6 3.9 1.7-7.4L1.5 9.1l7.4-.6z"/></svg>
    <svg width="26" height="26" viewBox="0 0 24 24"><path fill="var(--star)" d="M12 1.5l3.1 7 7.4.6-5.6 4.9 1.7 7.4L12 17.5l-6.6 3.9 1.7-7.4L1.5 9.1l7.4-.6z"/></svg>
    <svg width="26" height="26" viewBox="0 0 24 24"><path fill="var(--star)" d="M12 1.5l3.1 7 7.4.6-5.6 4.9 1.7 7.4L12 17.5l-6.6 3.9 1.7-7.4L1.5 9.1l7.4-.6z"/></svg>
    <svg width="26" height="26" viewBox="0 0 24 24"><path fill="var(--star)" d="M12 1.5l3.1 7 7.4.6-5.6 4.9 1.7 7.4L12 17.5l-6.6 3.9 1.7-7.4L1.5 9.1l7.4-.6z"/></svg>
  </div>
  <h3 class="abs t-title" style="left:590px;width:300px;text-align:right;top:1188px">Loved It</h3>
  <p class="abs t-quote" style="left:390px;width:500px;text-align:right;top:1235px">“JORDAN knows his stuff. Love his teaching style.”</p>
  <div class="abs avatar" style="left:922px;top:1186px" role="img" aria-label="Client avatar"></div>
  <p class="abs person" style="left:885px;top:1283px">Leo Marchetti</p>
  <div class="abs divider" style="top:1351px"></div>

  <!-- testimonial 3 -->
  <div class="abs avatar" style="left:190px;top:1403px" role="img" aria-label="Client avatar"></div>
  <p class="abs person" style="left:153px;top:1500px">Ryan Okafor</p>
  <h3 class="abs t-title" style="left:309px;top:1405px">The Right Coach</h3>
  <p class="abs t-quote" style="left:313px;top:1452px;width:690px">“Jordan was my first mentor and trainer in real estate. He pushed me from nobody to rookie of the year international. He is that person who will bring the best out of you! I am forever grateful for his coaching and mentorship! ”</p>
  <div class="abs stars" style="left:849px;top:1411px">
    <svg width="26" height="26" viewBox="0 0 24 24"><path fill="var(--star)" d="M12 1.5l3.1 7 7.4.6-5.6 4.9 1.7 7.4L12 17.5l-6.6 3.9 1.7-7.4L1.5 9.1l7.4-.6z"/></svg>
    <svg width="26" height="26" viewBox="0 0 24 24"><path fill="var(--star)" d="M12 1.5l3.1 7 7.4.6-5.6 4.9 1.7 7.4L12 17.5l-6.6 3.9 1.7-7.4L1.5 9.1l7.4-.6z"/></svg>
    <svg width="26" height="26" viewBox="0 0 24 24"><path fill="var(--star)" d="M12 1.5l3.1 7 7.4.6-5.6 4.9 1.7 7.4L12 17.5l-6.6 3.9 1.7-7.4L1.5 9.1l7.4-.6z"/></svg>
    <svg width="26" height="26" viewBox="0 0 24 24"><path fill="var(--star)" d="M12 1.5l3.1 7 7.4.6-5.6 4.9 1.7 7.4L12 17.5l-6.6 3.9 1.7-7.4L1.5 9.1l7.4-.6z"/></svg>
    <svg width="26" height="26" viewBox="0 0 24 24"><path fill="var(--star)" d="M12 1.5l3.1 7 7.4.6-5.6 4.9 1.7 7.4L12 17.5l-6.6 3.9 1.7-7.4L1.5 9.1l7.4-.6z"/></svg>
  </div>

  <p class="abs pager">1</p>
</main>

<section>
  <div class="abs news" role="img" aria-label="Overhead photo of people working at a wooden table with notebooks and coffee"></div>
  <div class="abs news-shade"></div>
  <h2 class="abs news-title">Subscribe To Our Newsletter</h2>
  <p class="abs news-sub">Join our mailing list and stay updated!</p>
  <div class="abs field" style="left:182px">Name</div>
  <div class="abs field" style="left:504px">Email</div>
  <a class="abs subscribe">Subscribe Now</a>
</section>

<footer>
  <div class="abs foot-brand">Bright Summit<br>Consulting</div>
  <nav class="foot-nav">
    <a class="active" style="left:370px">Home</a>
    <a style="left:462px">About</a>
    <a style="left:555px">Services</a>
    <a style="left:663px">Testimonails</a>
    <a style="left:809px">Contact</a>
  </nav>
  <a class="abs social" style="left:975px;background:var(--red)" aria-label="Social profile"></a>
  <a class="abs social" style="left:1028px;background:var(--muted)" aria-label="Social profile"></a>
  <p class="abs copyright">© 2019 by Bright Summit Consulting LLC. All rights reserved.</p>
</footer>

</body>
</html>
```